Powerpoint template for basic scientists studying immunology

We are an QVA-funded consortium of basic science researchers at academic centers in Boston, Philadelphia and Oxford, UK. We study why the immune system fails to get rid of Hepatitis C virus, and whether new antiviral treatments that reduce viral load improve immune function. We are looking for a powerpoint template that we can use as a "brand" for our research consortium. It would feature a logo (file attached) and should represent the fonts/colors contained in the logo. We we would present at meetings and to program officers at the QVA, but, if we ever get around to it, would also be on a website.

The scientific description is as follows:
Hepatitis C virus (HCV) infects 185 million persons worldwide, is the leading indication for liver transplantation and, in the US, has a higher mortaliy rate than HIV. The annual healthcare costs associated with HCV exceed $9 billion, a number expected to increase as the epidemic matures and end stage liver disease peaks over the next decade. By virtue of its remarkable predilection for persistence, HCV is a model chronic viral infection. Mounting evidence supports the idea that HCV, while inducing type I IFN expression, maintains chronicity by virtue of global suppression of host innate and adaptive immunity. The mainstay of treatment for the last two decades, IFN-α-based regimens are ineffective in many patient subgroups and have significant side effects. The recent development of highly effective direct acting antivirals (DAA) against HCV promises to alter the landscape of this devastating infection by offering curative therapy without IFN. However, it remains essential that we understand what type of immunity remains following pharmacological eradication of the virus because: a) many HCV infected subjects remain at risk for re-infection; and b) DAAs are only partially effective in some patient subgroups, particularly those with past treatment with IFN. The imminent availability of IFN-free treatment for HCV offers an unprecedented opportunity to understand broad questions about alterations in immunity in humans with cure of chronic infections. Until now, mechanistic dissection of human immune responses has been challenging due to limited ability to directly perturb the system. The organizing principle of this U19 Program therefore, is to capitalize on the unique opportunity to, for the first time, cure chronic viral infection in humans without immune modulation and interrogate the immunological changes that ensue. Thus, we have formulated the following central hypothesis for this Program: DAA-mediated cure of chronic HCV infection will lead to partial "resetting" of some immune abnormalities, but specific immunological defects will persist in some subjects that prevent development of optimal immunity to HCV. We will test this hypothesis through a set of integrated Projects and Cores.

Target Market(s)

scientists.

Industry/Entity Type

Biotechnology

Font styles to use
Sans Serif

Requirements
Must have
• Very clean, very simple. Mostly whitespace for puting graphs and data on. Colors, fonts should match the logo. Please see ppt example.
Should not have
• too much of the ppt covered with the logo.

```html
<!DOCTYPE html>
<html lang="en">
<head>
<meta charset="utf-8">
<title>KLV Orbis Consortium – Slide Template</title>
<link href="https://fonts.googleapis.com/css2?family=Figtree:wght@400;600;700;800&display=swap" rel="stylesheet">
<style>
:root{
  --blue:#0aa0df;
  --green:#4aa71c;
  --green-light:#66b733;
  --dark:#2d2d2d;
  --darker:#222;
  --ink:#333;
  --grey-row:#cfcfcf;
  --grey-head:#b5b5b5;
  --white:#fff;
}
*{box-sizing:border-box;margin:0;padding:0}
html,body{width:1061px;height:1200px;overflow:hidden;background:#000}
body{position:relative;font-family:"Figtree",Arial,sans-serif;color:var(--ink)}
.slide{position:absolute;width:518px;height:390px;overflow:hidden}
.col-a{left:8px}.col-b{left:535px}
.row-1{top:8px}.row-2{top:406px}.row-3{top:803px}

/* dark slides */
.slide--dark{background:radial-gradient(ellipse at 30% 30%,#4a4a4a 0%,#2c2c2c 70%)}
.slide--dark .top-band{position:absolute;left:0;top:0;width:100%;height:9px;background:var(--blue)}
.slide--dark .blue-band{position:absolute;left:0;top:290px;width:100%;height:48px;background:var(--blue)}
.slide--dark .footer{position:absolute;left:0;top:338px;width:100%;height:52px;background:var(--darker);display:flex;align-items:center;justify-content:space-between;padding:0 30px 0 30px}
.brand{display:flex;align-items:center;gap:8px;color:#e6e6e6;font-weight:400;letter-spacing:.5px;white-space:nowrap}
.brand-dot{width:20px;height:20px;border-radius:50%;background:#e6e6e6}
.slide--dark .brand{font-size:17px}
.presenter{text-align:right;color:var(--white);font-size:13px;line-height:17px}
.presenter b{display:block;color:var(--blue);font-size:15px;font-weight:700}

.title-block{position:absolute;left:45px;top:58px}
.title-block .t1{color:var(--blue);font-size:46px;font-weight:800;line-height:44px}
.title-block .t2{color:var(--white);font-size:50px;font-weight:800;line-height:50px}
.title-block .sub{color:var(--white);font-size:24px;font-weight:400;line-height:30px}
.title-block .sub span{color:var(--blue)}
.title-block p{color:#e8e8e8;font-size:12.5px;line-height:16px;margin-top:12px;width:330px}
.chevron{position:absolute;left:417px;top:63px}

.thanks{position:absolute;right:34px;top:55px;text-align:right;font-weight:800;font-size:72px;line-height:64px}
.thanks .a{color:var(--blue)}.thanks .b{color:var(--white)}

/* light slides */
.slide--light{background:linear-gradient(180deg,#fff 0%,#f2f2f2 70%,#e0e0e0 100%)}
.slide--light .top-band{position:absolute;left:0;top:0;width:100%;height:9px;background:var(--green)}
.slide--light .footer{position:absolute;left:0;top:350px;width:100%;height:40px;background:var(--darker);border-top:4px solid var(--green);display:flex;align-items:center;justify-content:space-between;padding:0 12px 0 22px}
.slide--light .brand{font-size:13px}
.slide--light .brand-dot{width:16px;height:16px}
.nav{display:flex;align-items:center;gap:5px;color:#ddd;font-size:12px}
.nav-btn{width:21px;height:19px;background:var(--green);border-radius:2px;display:flex;align-items:center;justify-content:center}
.page-no{border-left:1px solid #888;height:22px;margin-left:10px;padding-left:12px;display:flex;align-items:center}
.heading{position:absolute;left:22px;top:18px;font-size:28px;font-weight:800;color:var(--ink)}
.heading span{color:var(--green)}

.about{position:absolute;left:22px;top:72px;width:476px;font-size:13.5px;line-height:17px;color:#333;text-align:justify}
.about p{margin-bottom:12px}
.about b{color:var(--green);font-weight:700}

.services{position:absolute;left:40px;top:64px;list-style:none}
.services li{font-size:18px;font-weight:600;line-height:24.8px;display:flex;align-items:center;gap:12px}
.services li::before{content:"";width:6px;height:6px;background:var(--green);transform:rotate(45deg)}
.team-photo{position:absolute;left:228px;top:80px;width:268px;height:232px;background:radial-gradient(ellipse at 50% 55%,#3a3d44 0%,#6b6e75 45%,rgba(240,240,240,0) 75%)}

.data-table{position:absolute;left:25px;top:73px;width:468px;border-collapse:collapse;font-size:9.5px}
.data-table th{height:25px;font-size:13px;font-weight:700}
.data-table th.cat{background:var(--grey-head);color:#333}
.data-table th.o1{background:var(--green);color:var(--white)}
.data-table th.o2{background:#444;color:var(--white)}
.data-table td{height:18px;text-align:center}
.data-table tr.group td{background:var(--grey-row);text-align:left;padding-left:6px;font-weight:700;font-size:10px;color:#333}
.data-table td.label{text-align:left;padding-left:28px;background:#fff;color:#444}
.data-table tr.alt td.label{background:#f2f2f2}
.data-table td.y{background:var(--green);color:var(--white);width:116px}
.data-table tr.alt td.y{background:var(--green-light)}
.data-table td.n{background:#454545;color:#ddd;width:119px}
.data-table tr.alt td.n{background:#5a5a5a}

.map{position:absolute;left:32px;top:73px;width:220px;height:221px;border:4px solid #fff;box-shadow:0 0 3px rgba(0,0,0,.35);background:linear-gradient(160deg,#e8e4d2 0%,#dcd9c3 45%,#a9c8e6 70%,#9ec0e2 100%)}
.contact{position:absolute;left:266px;top:72px;width:240px;font-size:9.5px;line-height:11.5px;color:#444}
.contact .intro{text-align:justify;margin-bottom:8px}
.contact .intro b{color:var(--green)}
.contact h4{color:var(--green);font-size:11.5px;font-weight:700;margin-top:6px;line-height:14px}
.social{position:absolute;left:35px;top:313px;display:flex;align-items:center;gap:7px;font-size:12px;font-weight:600;color:#333}
.social i{width:18px;height:18px;background:var(--green);border-radius:2px}
.social span{color:var(--green)}
</style>
</head>
<body>

<section class="slide slide--dark col-a row-1">
  <div class="top-band"></div>
  <div class="title-block">
    <div class="t1">TITLE</div>
    <div class="t2">PROJECT</div>
    <div class="sub">subtext <span>presentation</span></div>
    <p>Lorem ipsum dolor sit amet, consectetuer adipiscing elit. Maecenas porttitor congue massa.</p>
  </div>
  <svg class="chevron" width="56" height="108" viewBox="0 0 56 108"><polygon points="0,0 56,54 0,108 0,88 34,54 0,20" fill="#fff"/></svg>
  <div class="blue-band"></div>
  <div class="footer">
    <div class="brand"><i class="brand-dot"></i>KLV ORBIS CONSORTIUM</div>
    <div class="presenter">Presentation by<b>Dana Reyes</b></div>
  </div>
</section>

<section class="slide slide--light col-b row-1">
  <div class="top-band"></div>
  <h2 class="heading"><span>About</span> Company</h2>
  <div class="about">
    <p><b>Lorem ipsum</b> dolor sit amet, consectetuer adipiscing elit. Maecenas porttitor congue massa. Fusce posuere, magna sed pulvinar ultricies, purus lectus malesuada libero, sit amet commodo magna eros quis urna.</p>
    <p><b>Nunc viverra imperdiet enim</b>. Fusce est. Vivamus a tellus. Pellentesque habitant morbi tristique senectus et netus et malesuada fames ac turpis egestas. Proin pharetra nonummy pede. Mauris et orci.</p>
    <p><b>Aenean nec lorem.</b> In porttitor. Donec laoreet nonummy augue.</p>
    <p>Suspendisse dui purus, scelerisque at, vulputate vitae, pretium mattis, nunc. Mauris eget neque at sem venenatis eleifend. Ut nonummy.</p>
    <p><b>Fusce aliquet pede non pede</b>.<br>Suspendisse dapibus lorem pellentesque magna. Integer nulla.</p>
  </div>
  <div class="footer">
    <div class="brand"><i class="brand-dot"></i>KLV ORBIS CONSORTIUM</div>
    <div class="nav">
      <span class="nav-btn"><svg width="9" height="11" viewBox="0 0 9 11"><polyline points="7,1 2,5.5 7,10" fill="none" stroke="#fff" stroke-width="2.5"/></svg></span>
      <span class="nav-btn"><svg width="9" height="11" viewBox="0 0 9 11"><polyline points="2,1 7,5.5 2,10" fill="none" stroke="#fff" stroke-width="2.5"/></svg></span>
      <span class="page-no">2</span>
    </div>
  </div>
</section>

<section class="slide slide--light col-a row-2">
  <div class="top-band"></div>
  <h2 class="heading"><span>Our</span> Services</h2>
  <ul class="services">
    <li>Lorem ipsum</li><li>Lorem ipsum</li><li>Lorem ipsum</li><li>Lorem ipsum</li><li>Lorem ipsum</li>
    <li>Lorem ipsum</li><li>Lorem ipsum</li><li>Lorem ipsum</li><li>Lorem ipsum</li><li>Lorem ipsum</li>
  </ul>
  <div class="team-photo" role="img" aria-label="Photo of a business team standing together in dark suits"></div>
  <div class="footer">
    <div class="brand"><i class="brand-dot"></i>KLV ORBIS CONSORTIUM</div>
    <div class="nav">
      <span class="nav-btn"><svg width="9" height="11" viewBox="0 0 9 11"><polyline points="7,1 2,5.5 7,10" fill="none" stroke="#fff" stroke-width="2.5"/></svg></span>
      <span class="nav-btn"><svg width="9" height="11" viewBox="0 0 9 11"><polyline points="2,1 7,5.5 2,10" fill="none" stroke="#fff" stroke-width="2.5"/></svg></span>
      <span class="page-no">3</span>
    </div>
  </div>
</section>

<section class="slide slide--light col-b row-2">
  <div class="top-band"></div>
  <h2 class="heading"><span>Table</span> Presentation</h2>
  <table class="data-table">
    <tr><th class="cat">CATEGORY</th><th class="o1">OPTION 1</th><th class="o2">OPTION 2</th></tr>
    <tr class="group"><td colspan="3">Category 1</td></tr>
    <tr><td class="label">Lorem ipsum dolor sit amet</td><td class="y">Yes</td><td class="n">-</td></tr>
    <tr class="alt"><td class="label">Lorem ipsum dolor sit amet</td><td class="y">Yes</td><td class="n">-</td></tr>
    <tr><td class="label">Lorem ipsum dolor sit amet</td><td class="y">Yes</td><td class="n">-</td></tr>
    <tr class="group"><td colspan="3">Category 2</td></tr>
    <tr><td class="label">Lorem ipsum dolor sit amet</td><td class="y">Yes</td><td class="n">-</td></tr>
    <tr class="alt"><td class="label">Lorem ipsum dolor sit amet</td><td class="y">Yes</td><td class="n">-</td></tr>
    <tr><td class="label">Lorem ipsum dolor sit amet</td><td class="y">Yes</td><td class="n">-</td></tr>
    <tr class="alt"><td class="label">Lorem ipsum dolor sit amet</td><td class="y">Yes</td><td class="n">-</td></tr>
    <tr class="group"><td colspan="3">Category 3</td></tr>
    <tr><td class="label">Lorem ipsum dolor sit amet</td><td class="y">Yes</td><td class="n">-</td></tr>
    <tr class="alt"><td class="label">Lorem ipsum dolor sit amet</td><td class="y">Yes</td><td class="n">-</td></tr>
  </table>
  <div class="footer">
    <div class="brand"><i class="brand-dot"></i>KLV ORBIS CONSORTIUM</div>
    <div class="nav">
      <span class="nav-btn"><svg width="9" height="11" viewBox="0 0 9 11"><polyline points="7,1 2,5.5 7,10" fill="none" stroke="#fff" stroke-width="2.5"/></svg></span>
      <span class="nav-btn"><svg width="9" height="11" viewBox="0 0 9 11"><polyline points="2,1 7,5.5 2,10" fill="none" stroke="#fff" stroke-width="2.5"/></svg></span>
      <span class="page-no">4</span>
    </div>
  </div>
</section>

<section class="slide slide--light col-a row-3">
  <div class="top-band"></div>
  <h2 class="heading"><span>Contact</span> Info</h2>
  <div class="map" role="img" aria-label="Map of the office location region"></div>
  <div class="contact">
    <p class="intro"><b>Lorem ipsum</b> dolor sit amet, consectetuer adipiscing elit. Maecenas porttitor congue massa. Fusce posuere, magna sed pulvinar ultricies, purus lectus malesuada libero, sit amet commodo magna eros quis urna.</p>
    <h4>Address</h4>
    <p>1234 Street Address<br>Harbor City, America<br>67890 (U.S.A)</p>
    <h4>Phone</h4><p>0123-456-789</p>
    <h4>FAX</h4><p>0123-456-789</p>
    <h4>Email</h4><p>info@yourcompany.com</p>
    <h4>Website</h4><p>www.yourcompany.com</p>
  </div>
  <div class="social"><i></i><i></i><i></i><i></i>@YOUR<span>COMPANY</span></div>
  <div class="footer">
    <div class="brand"><i class="brand-dot"></i>KLV ORBIS CONSORTIUM</div>
    <div class="nav">
      <span class="nav-btn"><svg width="9" height="11" viewBox="0 0 9 11"><polyline points="7,1 2,5.5 7,10" fill="none" stroke="#fff" stroke-width="2.5"/></svg></span>
      <span class="nav-btn"><svg width="9" height="11" viewBox="0 0 9 11"><polyline points="2,1 7,5.5 2,10" fill="none" stroke="#fff" stroke-width="2.5"/></svg></span>
      <span class="page-no">5</span>
    </div>
  </div>
</section>

<section class="slide slide--dark col-b row-3">
  <div class="top-band"></div>
  <div class="thanks"><div class="a">Thank</div><div class="b">You</div></div>
  <div class="blue-band"></div>
  <div class="footer">
    <div class="brand"><i class="brand-dot"></i>KLV ORBIS CONSORTIUM</div>
    <div class="presenter">Presentation by<b>Dana Reyes</b></div>
  </div>
</section>

</body>
</html>
```